Website for courses for men for making money, health, fitness

I require a website which is going to be a mix of a crypto currency website and website aimed at providing men with money making, health, relationship advice courses and content

The name isn't decided yet so for now please call it something like

VANTAGE DEN

A platform dedicated to making men wealthy, physically strong, mentally tough & successful with women

In the top right, I need it to show how many points they have, they must buy points in order to use them to claim the courses.

WHAT WE DO

Vantage den is a platform where you can learn everything you need about business, making money, crypto currency, fitness, health, mental toughness and resilience and how to be successful with women all in one place

HOW WILL THIS WORK & WHY SHOULD I BUY POINTS?

xxxxxxxxxxxxxxxxxxxxxxxx
xxxxxxxxxxxxxxxxxxxxxxx
xxxxxxxxxxxxxxxxxxxxx

AFFILIATE SCHEME

EARN UP TO $125 DOLLARS PER PERSON WHO SIGNS UP THROUGH YOUR LINK

START EARNING NOW - button
______________________________________________________

BUY POINTS
(A maximum of only $250 worth of points can be purchased per person until the platform goes fully live)

ROAD MAP & THE MODEL

2023

Q1 - PRE BUY IN FOR POINTS

Q2 - FULL WEBSITE LAUNCH

Q3 - APP LAUNCH

Q4 - IN APP ADVERT LAUNCH

It must have a very slick and sharp eye catching look, and be designed to convert people into purchasing points

some ideas of the feel of the website -

https://brelvora.io/
https://plimwick.style/
https://fable.korvell.com/

```html
<!DOCTYPE html>
<html lang="en">
<head>
<meta charset="utf-8">
<title>Vantage Den</title>
<link href="https://fonts.googleapis.com/css2?family=Poppins:wght@400;500;600;700;800&display=swap" rel="stylesheet">
<style>
:root{
  --navy:#1b3a6b;
  --orange:#f26b1d;
  --ink:#333a45;
  --hero-deep:#0b2a9e;
  --hero-bright:#2a5df0;
  --grey-band:#f3f3f3;
  --card-line:#c9cfdc;
  --arc:#a9b3c8;
  --frame:#d9dee8;
  --dark-band:#0b1a3a;
  --road-deep:#08155a;
  --road-bright:#0e2a8c;
  --footer:#222222;
  --footer-text:#e6e6e6;
  --white:#ffffff;
}
*{margin:0;padding:0;box-sizing:border-box}
html,body{width:1200px;height:4385px;overflow:hidden;background:var(--white)}
body{font-family:'Poppins',sans-serif;color:var(--ink)}
.page{position:relative;width:1200px;height:4385px;overflow:hidden}
.abs{position:absolute}
.center{left:0;width:1200px;text-align:center}

/* header */
.site-header{position:absolute;top:0;left:0;width:1200px;height:95px;background:var(--white);z-index:3}
.brand{position:absolute;left:75px;top:30px;font-weight:800;font-size:29px;color:var(--navy);letter-spacing:.5px}
.main-nav{position:absolute;left:354px;top:38px;display:flex;gap:32px;font-size:15px;font-weight:500;color:#333}
.btn-pill{position:absolute;display:flex;align-items:center;justify-content:center;border-radius:30px;font-weight:600}
.btn-signup{left:878px;top:27px;width:116px;height:44px;border:2px solid var(--orange);color:var(--orange);font-size:17px}
.btn-login{left:1009px;top:27px;width:116px;height:44px;border:2px solid var(--navy);color:var(--navy);font-size:17px}

/* hero */
.hero-bg{position:absolute;top:0;left:0}
.hero-title{top:262px;font-size:88px;font-weight:700;color:var(--white);letter-spacing:2px;line-height:1}
.hero-sub{top:360px;font-size:24px;line-height:37px;color:var(--white);font-weight:500}
.btn-solid{background:var(--orange);color:var(--white)}
.btn-outline{border:2px solid var(--orange);color:var(--orange);background:var(--white)}
.hero-cta{left:497px;top:454px;width:206px;height:55px;font-size:19px}

/* what we do */
.h2{font-weight:700;color:var(--navy)}
.what-title{top:825px;font-size:40px}
.what-text{top:892px;font-size:19px;line-height:35px;color:#444}
.what-cta{left:497px;top:1031px;width:206px;height:55px;font-size:19px}

/* how it works */
.how-band{position:absolute;top:1159px;left:0;width:1200px;height:526px;background:var(--grey-band)}
.how-title{top:1222px;font-size:40px}
.step-card{position:absolute;top:1331px;width:240px;height:248px;background:var(--white);border:2px solid var(--card-line);border-radius:22px;text-align:center}
.step-icon{position:absolute;left:90px;top:24px}
.step-name{position:absolute;top:98px;left:0;width:100%;font-size:23px;font-weight:700;color:var(--navy)}
.step-text{position:absolute;top:136px;left:0;width:100%;font-size:16px;line-height:27px;color:#444}

/* split sections */
.split-title{font-size:38px;font-weight:700;color:var(--navy)}
.split-text{font-size:19.5px;line-height:35px;color:#444}
.why-title{left:614px;top:1820px}
.why-text{left:614px;top:1889px;width:520px}
.why-cta{left:618px;top:2097px;width:206px;height:55px;font-size:19px}

/* affiliate */
.aff-title{top:2428px;font-size:38px;font-weight:700;color:var(--white)}
.aff-sub{top:2494px;font-size:33px;line-height:48px;color:var(--white)}
.aff-cta{left:478px;top:2626px;width:242px;height:55px;font-size:19px}

.buy-title{left:73px;top:2993px;font-size:40px}
.buy-text{left:73px;top:3062px;width:500px}
.buy-cta{left:75px;top:3196px;width:208px;height:55px;font-size:19px}

/* roadmap */
.road-title{top:3540px;font-size:37px;font-weight:700;color:var(--white)}
.milestone{position:absolute;top:3638px;width:250px;text-align:center;color:var(--white)}
.milestone .quarter{font-size:22px;font-weight:700}
.milestone .tick{margin:22px auto 0;width:74px;height:74px;border-radius:50%;background:var(--orange);display:flex;align-items:center;justify-content:center}
.milestone .name{margin-top:18px;font-size:19px;font-weight:700}
.milestone .desc{margin-top:4px;font-size:15.5px;line-height:25px}
.road-line{position:absolute;top:3718px;left:196px;width:808px;border-top:2px dashed var(--white)}

/* footer */
.site-footer{position:absolute;top:3971px;left:0;width:1200px;height:414px;background:var(--footer);color:var(--footer-text)}
.foot-col{position:absolute;top:57px}
.foot-col h4{font-size:17px;font-weight:700;color:var(--white);letter-spacing:.3px;margin-bottom:8px}
.foot-col li{list-style:none;font-size:15px;line-height:33px}
.news-text{font-size:15px;line-height:25px;width:330px}
.email-box{margin-top:14px;width:330px;height:54px;border:1.5px solid #bbb;border-radius:30px;display:flex;align-items:center;justify-content:space-between;padding:0 20px 0 24px;font-size:15px}
.follow{margin-top:24px}
.socials{display:flex;gap:22px;margin-top:10px}
.social-box{width:30px;height:30px;border:2px solid #bbb;border-radius:5px}
.foot-rule{position:absolute;top:347px;left:0;width:1200px;border-top:1px solid #444}
.copyright{position:absolute;top:371px;left:0;width:1200px;text-align:center;font-size:14px}
</style>
</head>
<body>
<div class="page">

  <!-- hero background -->
  <svg class="hero-bg" width="1200" height="800" viewBox="0 0 1200 800" role="img" aria-label="Blue toned photo of stacked digital coins over a glowing trading chart">
    <defs>
      <linearGradient id="heroGrad" x1="0" y1="0" x2="1" y2="1">
        <stop offset="0" stop-color="#1f4fe0"/>
        <stop offset=".55" stop-color="#0b2a9e"/>
        <stop offset="1" stop-color="#2a5df0"/>
      </linearGradient>
    </defs>
    <path d="M0,95 H1200 V715 C1000,770 800,738 600,752 C400,764 260,770 150,735 C80,712 30,672 0,655 Z" fill="url(#heroGrad)"/>
  </svg>

  <header class="site-header">
    <div class="brand">VANTAGE DEN</div>
    <nav class="main-nav"><span>What We Do</span><span>How it Works</span><span>Road Map</span><span>Blog</span><span>Contact</span></nav>
    <div class="btn-pill btn-signup">Sign Up</div>
    <div class="btn-pill btn-login">Login</div>
  </header>

  <h1 class="abs center hero-title">VANTAGE DEN</h1>
  <p class="abs center hero-sub">A platform dedicated to making men wealthy, physically strong,<br>mentally tough &amp; successful with women.</p>
  <div class="btn-pill btn-solid hero-cta">Learn More</div>

  <!-- what we do -->
  <h2 class="abs center h2 what-title">What We Do</h2>
  <p class="abs center what-text">Vantage den is a platform where you can learn everything you need about business,<br>making money, crypto currency, fitness, health, mental toughness and resilience and how<br>to be successful with women all in one place.</p>
  <div class="btn-pill btn-outline what-cta">Learn More</div>

  <!-- how it works -->
  <div class="how-band"></div>
  <h2 class="abs center h2 how-title">How Will This Work</h2>
  <svg class="abs" style="left:0;top:1280px" width="1200" height="360" viewBox="0 1280 1200 360">
    <path d="M470,1331 C540,1292 660,1292 730,1331" fill="none" stroke="var(--arc)" stroke-width="4"/>
    <path d="M205,1579 C250,1615 400,1615 455,1579" fill="none" stroke="var(--arc)" stroke-width="4"/>
    <path d="M735,1579 C780,1615 930,1615 985,1579" fill="none" stroke="var(--arc)" stroke-width="4"/>
  </svg>

  <div class="step-card" style="left:75px">
    <svg class="step-icon" width="60" height="62" viewBox="0 0 60 62" fill="none" stroke="var(--orange)" stroke-width="2.2">
      <rect x="6" y="4" width="30" height="40" rx="2"/><rect x="12" y="10" width="30" height="40" rx="2" fill="#fff"/>
      <line x1="18" y1="22" x2="36" y2="22"/><line x1="18" y1="30" x2="36" y2="30"/><line x1="18" y1="38" x2="28" y2="38"/>
      <circle cx="44" cy="48" r="9" fill="#fff"/><path d="M39,48 l4,4 l6,-7"/>
    </svg>
    <div class="step-name">Sign Up</div>
    <div class="step-text">Sed ut perspiciatis<br>unde omnis iste natus<br>error sit volup.</div>
  </div>
  <div class="step-card" style="left:345px">
    <svg class="step-icon" width="62" height="62" viewBox="0 0 62 62" fill="none" stroke="var(--orange)" stroke-width="2.2">
      <circle cx="36" cy="24" r="18"/><path d="M30,28 a7,7 0 1 1 12,0 l-1,5 h-10 z"/><line x1="32" y1="36" x2="40" y2="36"/>
      <line x1="23" y1="37" x2="6" y2="56" stroke-width="4"/>
    </svg>
    <div class="step-name">Explore</div>
    <div class="step-text">Sed ut perspiciatis<br>unde omnis iste natus<br>error sit volup.</div>
  </div>
  <div class="step-card" style="left:614px">
    <svg class="step-icon" width="60" height="62" viewBox="0 0 60 62" fill="none" stroke="var(--orange)" stroke-width="2.2">
      <path d="M4,6 h8 l6,34 h32 l4,-20 h-10"/><circle cx="34" cy="16" r="11"/><path d="M29,16 l4,4 l6,-7"/>
      <circle cx="22" cy="52" r="4"/><circle cx="44" cy="52" r="4"/>
    </svg>
    <div class="step-name">Checkout</div>
    <div class="step-text">Sed ut perspiciatis<br>unde omnis iste natus<br>error sit volup.</div>
  </div>
  <div class="step-card" style="left:885px">
    <svg class="step-icon" width="62" height="62" viewBox="0 0 62 62" fill="none" stroke="var(--orange)" stroke-width="2.2">
      <rect x="4" y="6" width="54" height="38" rx="2"/><line x1="31" y1="44" x2="31" y2="54"/><line x1="18" y1="56" x2="44" y2="56"/>
      <path d="M12,34 l10,-10 l8,6 l14,-16"/><path d="M38,14 h6 v6"/>
    </svg>
    <div class="step-name">Earn Points</div>
    <div class="step-text">Sed ut perspiciatis<br>unde omnis iste natus<br>error sit volup.</div>
  </div>

  <!-- why buy points -->
  <svg class="abs" style="left:60px;top:1735px" width="560" height="520" viewBox="0 0 560 520">
    <defs>
      <linearGradient id="whyGrad" x1="0" y1="0" x2="1" y2="1">
        <stop offset="0" stop-color="#6fb3d6"/><stop offset=".5" stop-color="#2c3646"/><stop offset="1" stop-color="#b9d4e6"/>
      </linearGradient>
    </defs>
    <path d="M70,12 Q80,5 100,8 L520,40 Q545,44 540,70 L480,470 Q474,500 445,498 L40,480 Q15,478 15,450 L15,60 Q15,28 70,12 Z" fill="var(--frame)"/>
    <path d="M40,44 H500 Q530,44 525,74 L480,395 Q472,422 445,428 L40,508 Q15,510 15,485 V70 Q15,44 40,44 Z" fill="url(#whyGrad)" role="img" aria-label="Photo of a man in glasses beside a glowing market chart"/>
  </svg>
  <h2 class="abs split-title why-title">Why Should I Buy Points?</h2>
  <p class="abs split-text why-text">Sed ut perspiciatis unde omnis iste natus error sit voluptatem accusantium doloremque laudantium, totam rem aperiam, eaque ipsa quae ab illo inventore veritatis et quasi architecto beatae vitae dicta sunt explicabo.</p>
  <div class="btn-pill btn-outline why-cta">Learn More</div>

  <!-- affiliate -->
  <svg class="abs" style="left:0;top:2230px" width="1200" height="640" viewBox="0 2230 1200 640" role="img" aria-label="Dark blue photo of a team meeting around a table">
    <defs>
      <linearGradient id="affGrad" x1="0" y1="0" x2="1" y2="1">
        <stop offset="0" stop-color="#0a1630"/><stop offset=".5" stop-color="#1a2d52"/><stop offset="1" stop-color="#0b1a3a"/>
      </linearGradient>
    </defs>
    <path d="M0,2408 C200,2360 400,2350 600,2370 C850,2395 1050,2320 1200,2238 V2720 C1050,2770 900,2760 750,2745 C550,2725 350,2750 200,2790 C120,2812 50,2840 0,2860 Z" fill="url(#affGrad)"/>
  </svg>
  <h2 class="abs center aff-title">Affiliate Scheme</h2>
  <p class="abs center aff-sub">Earn up to $125 dollars per person who<br>signs up through your link.</p>
  <div class="btn-pill btn-solid aff-cta">Start Earning Now</div>

  <!-- buy points -->
  <h2 class="abs split-title buy-title">Buy Points</h2>
  <p class="abs split-text buy-text">A maximum of only $250 worth of points can be purchased per person until the platform goes fully live.</p>
  <div class="btn-pill btn-outline buy-cta">Learn More</div>
  <svg class="abs" style="left:595px;top:2870px" width="545" height="520" viewBox="0 0 545 520">
    <defs>
      <linearGradient id="buyGrad" x1="0" y1="0" x2="1" y2="1">
        <stop offset="0" stop-color="#cfd6df"/><stop offset=".45" stop-color="#2a3340"/><stop offset="1" stop-color="#15233b"/>
      </linearGradient>
    </defs>
    <path d="M480,8 Q505,6 510,30 L530,470 Q530,500 500,502 L90,505 Q62,505 58,478 L8,150 Q5,125 30,118 Z" fill="var(--frame)"/>
    <path d="M60,44 H500 Q530,44 530,74 V480 Q530,510 500,506 L90,480 Q62,476 55,450 L20,80 Q18,44 60,44 Z" fill="url(#buyGrad)" role="img" aria-label="Photo of a man pointing at trading charts on computer screens"/>
  </svg>

  <!-- roadmap -->
  <svg class="abs" style="left:0;top:3330px" width="1200" height="645" viewBox="0 3330 1200 645" role="img" aria-label="Deep blue network pattern background">
    <defs>
      <linearGradient id="roadGrad" x1="0" y1="0" x2="1" y2="1">
        <stop offset="0" stop-color="#08155a"/><stop offset=".5" stop-color="#0e2a8c"/><stop offset="1" stop-color="#08155a"/>
      </linearGradient>
    </defs>
    <path d="M0,3362 C150,3400 300,3430 500,3420 C700,3410 800,3380 950,3385 C1050,3388 1130,3395 1200,3380 V3975 H0 Z" fill="url(#roadGrad)"/>
  </svg>
  <h2 class="abs center road-title">Road Map &amp; The Model</h2>
  <div class="road-line"></div>
  <div class="milestone" style="left:71px">
    <div class="quarter">Q1 2023</div>
    <div class="tick"><svg width="34" height="26" viewBox="0 0 34 26"><path d="M3,13 l10,10 l18,-20" fill="none" stroke="#fff" stroke-width="5" stroke-linecap="round"/></svg></div>
    <div class="name">Pre Buy In For Points</div>
    <div class="desc">Sed ut perspiciatis unde omnis<br>iste natus error sit voluptatem<br>accusantium</div>
  </div>
  <div class="milestone" style="left:338px">
    <div class="quarter">Q2 2023</div>
    <div class="tick"><svg width="34" height="26" viewBox="0 0 34 26"><path d="M3,13 l10,10 l18,-20" fill="none" stroke="#fff" stroke-width="5" stroke-linecap="round"/></svg></div>
    <div class="name">Full Website Launch</div>
    <div class="desc">Sed ut perspiciatis unde omnis<br>iste natus error sit voluptatem<br>accusantium</div>
  </div>
  <div class="milestone" style="left:610px">
    <div class="quarter">Q3 2023</div>
    <div class="tick"><svg width="34" height="26" viewBox="0 0 34 26"><path d="M3,13 l10,10 l18,-20" fill="none" stroke="#fff" stroke-width="5" stroke-linecap="round"/></svg></div>
    <div class="name">App Launch</div>
    <div class="desc">Sed ut perspiciatis unde omnis<br>iste natus error sit voluptatem<br>accusantium</div>
  </div>
  <div class="milestone" style="left:879px">
    <div class="quarter">Q4 2023</div>
    <div class="tick"><svg width="34" height="26" viewBox="0 0 34 26"><path d="M3,13 l10,10 l18,-20" fill="none" stroke="#fff" stroke-width="5" stroke-linecap="round"/></svg></div>
    <div class="name">In App Advert Launch</div>
    <div class="desc">Sed ut perspiciatis unde omnis<br>iste natus error sit voluptatem<br>accusantium</div>
  </div>

  <!-- footer -->
  <footer class="site-footer">
    <div class="foot-col" style="left:75px"><h4>COMPANY</h4><ul><li>Nemo enim ipsam</li><li>Voluptatem</li><li>Quia voluptas sit</li><li>Aspernatur aut</li><li>Odit aut fugitsed</li><li>Quia conse</li></ul></div>
    <div class="foot-col" style="left:305px"><h4>RESOURCES</h4><ul><li>Nemo enim ipsam</li><li>Voluptatem</li><li>Quia voluptas sit</li><li>Aspernatur aut</li></ul></div>
    <div class="foot-col" style="left:555px"><h4>HELP</h4><ul><li>Nemo enim ipsam</li><li>Voluptatem</li><li>Quia voluptas sit</li><li>Aspernatur aut</li><li>Odit aut fugitsed</li><li>Quia conse</li></ul></div>
    <div class="foot-col" style="left:795px">
      <h4>NEWSLETTER SIGN UP</h4>
      <p class="news-text">Nemo enim ipsam oluptatem uia voluptas sit spernatur autdit aut fugitsed.</p>
      <div class="email-box"><span>Email Address</span>
        <svg width="22" height="20" viewBox="0 0 22 20"><path d="M1,9 L21,1 L15,19 L10,12 Z" fill="var(--orange)"/></svg>
      </div>
      <h4 class="follow">FOLLOW US</h4>
      <div class="socials"><div class="social-box"></div><div class="social-box"></div><div class="social-box"></div><div class="social-box"></div></div>
    </div>
    <div class="foot-rule"></div>
    <p class="copyright">Copyright © 2022 CompanyName All rights reserved.</p>
  </footer>

</div>
</body>
</html>
```